Bright Acorns Business Card Design

Bright Acorns - Cultivating Natural Play Spaces

Bright Acorns is a company that focuses on promoting the design, construction, consultation and support of natural, creative and organic play spaces for Early Childhood and learning environments.

We need a professional Business Card designed that is unique modern and creative. The Philosophy of the company is nostalgic so the business and will need to reflect this but also reflect that our ideas are modern and cutting edge.

The business card will need to be a talking point, by either having a unique size, quality and/or placement of logo or other quality.

I am more interested in using natural recycled paper, as this would reflect the philosophy of the company, but I open to seeing colour used creatively.
Updates

Hi Designers, Apologies, Could you please add www.brightacorns.com.au to the business card. Thanks very much.

Hi All, Thank you all for your submission thus far. Please note the fonts for used in the logo are: Ostrich Sans Black and Archer Semi Bold. If these could be considered for contact details, my name etc. Also please show the design on a recycled brown card if possible as this will be the type of card I will use when printing. Thanks so much.

Target Market(s)

Child Care Providers, Play Industry Professionals

Industry/Entity Type

Business

Contact Information for Business Card

Bright Acorns
Designing Outdoor Learning Places
Marlene Okafor
0419 862 304
marlene@brightacorns.com.au

Font styles to use
Sans Serif

Requirements
Must have
• The Logo and the Details plus the below phrase
• Bright Acorns - Cultivating Natural Play Spaces
Nice to have
• A bit of colour, but not too much colour.
Should not have
• Not to have a white background, recycled brown card only

```html
<!DOCTYPE html>
<html lang="en">
<head>
<meta charset="utf-8">
<title>Bright Acorns Business Card Design</title>
<link rel="stylesheet" href="https://fonts.googleapis.com/css2?family=Bebas+Neue&family=Zilla+Slab:wght@500;600&display=swap">
<style>
  :root {
    --page: #ffffff;
    --kraft: #c6ad8a;
    --kraft-light: #cdb594;
    --kraft-dark: #bba07c;
    --ink: #0d6634;
  }
  html, body {
    margin: 0;
    padding: 0;
    width: 1200px;
    height: 900px;
    overflow: hidden;
    background: var(--page);
  }
  .canvas {
    position: relative;
    width: 1200px;
    height: 900px;
  }
  .card {
    position: absolute;
    top: 305px;
    width: 523px;
    height: 282px;
    clip-path: path('M0,100 C0,28 140,0 261.5,0 C383,0 523,28 523,100 L523,242 Q523,282 483,282 L40,282 Q0,282 0,242 Z');
    background:
      radial-gradient(ellipse at 30% 40%, var(--kraft-light), transparent 60%),
      radial-gradient(ellipse at 75% 70%, var(--kraft-dark), transparent 55%),
      var(--kraft);
    color: var(--ink);
    text-align: center;
  }
  .card--front { left: 60px; }
  .card--back { left: 613px; }

  .brand-dot {
    position: absolute;
    left: 226px;
    top: 62px;
    width: 70px;
    height: 70px;
    border-radius: 50%;
    background: var(--ink);
  }
  .brand-name {
    position: absolute;
    left: 0;
    right: 0;
    top: 150px;
    margin: 0;
    font-family: 'Bebas Neue', sans-serif;
    font-weight: 400;
    font-size: 46px;
    letter-spacing: 1px;
    line-height: 1;
  }
  .brand-tagline {
    position: absolute;
    left: 0;
    right: 0;
    top: 194px;
    margin: 0;
    font-family: 'Zilla Slab', serif;
    font-weight: 600;
    font-size: 11.5px;
    line-height: 1.2;
    text-transform: uppercase;
    letter-spacing: 0.3px;
  }

  .back-heading {
    position: absolute;
    left: 0;
    right: 0;
    top: 54px;
    margin: 0;
    font-family: 'Bebas Neue', sans-serif;
    font-weight: 400;
    font-size: 33px;
    letter-spacing: 1px;
    line-height: 1;
  }
  .back-tagline {
    position: absolute;
    left: 0;
    right: 0;
    top: 86px;
    margin: 0;
    font-family: 'Zilla Slab', serif;
    font-weight: 600;
    font-size: 11.5px;
  }
  .contact {
    position: absolute;
    left: 0;
    right: 0;
    top: 118px;
    font-family: 'Zilla Slab', serif;
    font-weight: 600;
    font-style: normal;
  }
  .contact__name {
    display: block;
    font-weight: 500;
    font-size: 20px;
    line-height: 26px;
  }
  .contact__line {
    display: block;
    font-size: 15px;
    line-height: 20px;
  }
  .back-mark {
    position: absolute;
    left: 192px;
    top: 198px;
    width: 140px;
    height: 140px;
    border-radius: 50%;
    background: var(--ink);
  }
</style>
</head>
<body>
  <main class="canvas">
    <section class="card card--front" aria-label="Card front">
      <span class="brand-dot" aria-hidden="true"></span>
      <h1 class="brand-name">Bright Acorns</h1>
      <p class="brand-tagline">Designing<br>Outdoor Learning Places</p>
    </section>

    <section class="card card--back" aria-label="Card back">
      <h2 class="back-heading">Bright Acorns</h2>
      <p class="back-tagline">Designing Outdoor Learning Places</p>
      <address class="contact">
        <span class="contact__name">Marlene Okafor</span>
        <span class="contact__line">0419 862 304</span>
        <span class="contact__line">marlene@brightacorns.com.au</span>
      </address>
      <span class="back-mark" aria-hidden="true"></span>
    </section>
  </main>
</body>
</html>
```